Verdant Solutions Business Card

want the back of card to be blue- with the logo in the center
front of card- info plus logo (info being mailing address, email address, and website address )
4 different names with titles to have on cards
1) Dalton Mirsky - Owner
2) Brenda Tolvin- Customer Relationship Specialist
3) Henri Kastner- Vice President of Sales
4) Wade Dunmor- Chief Technology Officer

Target Market(s)

tech company in the government/probation office industry

Industry/Entity Type

Government Office

Contact Information for Business Card

1) Dalton Mirsky - Owner

Colors
0355a3
ffffff

Requirements
Must have
• back side should be blue, with the logo placed in the center
• front side needs to include both the logo, as well as company info (info should include website address, email address, and mailing address)

```html
<!DOCTYPE html>
<html lang="en">
<head>
<meta charset="utf-8">
<title>Verdant Solutions Business Cards</title>
<link rel="stylesheet" href="https://fonts.googleapis.com/css2?family=Open+Sans:wght@400;600;700&display=swap">
<style>
:root{
  --blue:#0355a3;
  --white:#ffffff;
  --grey:#8c8f94;
  --stage:#3b3c3f;
  --divider:#2c2d30;
}
*{margin:0;padding:0;box-sizing:border-box}
html,body{width:1200px;height:2684px;overflow:hidden;background:var(--stage);font-family:"Open Sans",Arial,sans-serif}
.set{position:relative;width:1200px;height:671px;border-bottom:2px solid var(--divider)}
.set:last-child{border-bottom:0}
.card{position:absolute;width:530px;height:300px;border-radius:26px;overflow:hidden;box-shadow:0 12px 26px rgba(0,0,0,.45)}
.card-back{left:90px;top:40px;background:var(--blue);display:flex;align-items:center;justify-content:center}
.card-front{left:570px;top:352px;background:var(--blue)}
.card-front .shape{position:absolute;inset:0;width:100%;height:100%}
.brand{display:flex;align-items:center;gap:10px;font-weight:600;white-space:nowrap}
.brand-mark{width:20px;height:20px;background:currentColor;flex:none}
.card-back .brand{color:var(--white);font-size:30px}
.card-back .brand-mark{width:30px;height:30px}
.card-front .brand{position:absolute;left:305px;top:110px;color:var(--blue);font-size:18px;line-height:24px}
.person{position:absolute;left:35px;top:60px}
.person-name{color:var(--blue);font-weight:700;font-size:19px;line-height:24px;white-space:nowrap}
.person-title{color:var(--white);font-size:13px;line-height:18px;white-space:nowrap}
.contact{position:absolute;left:35px;top:160px;color:var(--white);font-size:12.5px;line-height:19px}
.contact li{list-style:none;display:flex;align-items:center;gap:7px;white-space:nowrap}
.contact .address{display:block;margin-bottom:4px}
.icon{width:13px;height:13px;flex:none}
</style>
</head>
<body>

<section class="set">
  <div class="card card-back"><div class="brand"><span class="brand-mark"></span>Verdant Solutions</div></div>
  <div class="card card-front">
    <svg class="shape" viewBox="0 0 530 300" aria-hidden="true">
      <polygon points="185,0 530,0 530,300 459,300" fill="#ffffff"/>
      <polygon points="178,0 185,0 459,300 450,300" fill="#8c8f94"/>
      <polygon points="0,58 230,58 283,117 0,117" fill="#8c8f94"/>
    </svg>
    <div class="person"><p class="person-name">Brenda Tolvin</p><p class="person-title">Customer Relationship Specialist</p></div>
    <div class="brand"><span class="brand-mark"></span>Verdant Solutions</div>
    <ul class="contact">
      <li class="address">Harlow Crossing<br>Fenmore Park, 2240</li>
      <li><svg class="icon" viewBox="0 0 14 14"><rect x=".5" y=".5" width="13" height="13" rx="2" fill="none" stroke="#fff"/><path d="M4 3.5l2 1-1 1.5c.6 1.2 1.3 1.9 2.5 2.5L9 7.5l1 2-1.5 1C6 10 4 8 3.5 5.5z" fill="#fff"/></svg>555-214-3380</li>
      <li><svg class="icon" viewBox="0 0 14 14"><rect x=".5" y=".5" width="13" height="13" rx="2" fill="none" stroke="#fff"/><rect x="4.5" y="3" width="5" height="8" rx="1" fill="none" stroke="#fff"/></svg>555-762-1045(office)</li>
      <li><svg class="icon" viewBox="0 0 14 14"><rect x=".5" y=".5" width="13" height="13" rx="2" fill="none" stroke="#fff"/><rect x="3" y="4.5" width="8" height="5.5" fill="none" stroke="#fff"/><path d="M3 4.5l4 3 4-3" fill="none" stroke="#fff"/></svg>hello@verdantsolutionsco.com</li>
      <li><svg class="icon" viewBox="0 0 14 14"><rect x=".5" y=".5" width="13" height="13" rx="2" fill="none" stroke="#fff"/><circle cx="7" cy="7" r="3.5" fill="none" stroke="#fff"/><path d="M3.5 7h7M7 3.5v7" stroke="#fff"/></svg>www.verdantsolutionsco.com</li>
    </ul>
  </div>
</section>

<section class="set">
  <div class="card card-back"><div class="brand"><span class="brand-mark"></span>Verdant Solutions</div></div>
  <div class="card card-front">
    <svg class="shape" viewBox="0 0 530 300" aria-hidden="true">
      <polygon points="185,0 530,0 530,300 459,300" fill="#ffffff"/>
      <polygon points="178,0 185,0 459,300 450,300" fill="#8c8f94"/>
      <polygon points="0,58 230,58 283,117 0,117" fill="#8c8f94"/>
    </svg>
    <div class="person"><p class="person-name">Dalton Mirsky</p><p class="person-title">Owner</p></div>
    <div class="brand"><span class="brand-mark"></span>Verdant Solutions</div>
    <ul class="contact">
      <li class="address">Harlow Crossing<br>Fenmore Park, 2240</li>
      <li><svg class="icon" viewBox="0 0 14 14"><rect x=".5" y=".5" width="13" height="13" rx="2" fill="none" stroke="#fff"/><path d="M4 3.5l2 1-1 1.5c.6 1.2 1.3 1.9 2.5 2.5L9 7.5l1 2-1.5 1C6 10 4 8 3.5 5.5z" fill="#fff"/></svg>555-214-3380</li>
      <li><svg class="icon" viewBox="0 0 14 14"><rect x=".5" y=".5" width="13" height="13" rx="2" fill="none" stroke="#fff"/><rect x="4.5" y="3" width="5" height="8" rx="1" fill="none" stroke="#fff"/></svg>555-762-1045(office)</li>
      <li><svg class="icon" viewBox="0 0 14 14"><rect x=".5" y=".5" width="13" height="13" rx="2" fill="none" stroke="#fff"/><rect x="3" y="4.5" width="8" height="5.5" fill="none" stroke="#fff"/><path d="M3 4.5l4 3 4-3" fill="none" stroke="#fff"/></svg>hello@verdantsolutionsco.com</li>
      <li><svg class="icon" viewBox="0 0 14 14"><rect x=".5" y=".5" width="13" height="13" rx="2" fill="none" stroke="#fff"/><circle cx="7" cy="7" r="3.5" fill="none" stroke="#fff"/><path d="M3.5 7h7M7 3.5v7" stroke="#fff"/></svg>www.verdantsolutionsco.com</li>
    </ul>
  </div>
</section>

<section class="set">
  <div class="card card-back"><div class="brand"><span class="brand-mark"></span>Verdant Solutions</div></div>
  <div class="card card-front">
    <svg class="shape" viewBox="0 0 530 300" aria-hidden="true">
      <polygon points="185,0 530,0 530,300 459,300" fill="#ffffff"/>
      <polygon points="178,0 185,0 459,300 450,300" fill="#8c8f94"/>
      <polygon points="0,58 230,58 283,117 0,117" fill="#8c8f94"/>
    </svg>
    <div class="person"><p class="person-name">Henri Kastner</p><p class="person-title">Vice President of Sales</p></div>
    <div class="brand"><span class="brand-mark"></span>Verdant Solutions</div>
    <ul class="contact">
      <li class="address">Harlow Crossing<br>Fenmore Park, 2240</li>
      <li><svg class="icon" viewBox="0 0 14 14"><rect x=".5" y=".5" width="13" height="13" rx="2" fill="none" stroke="#fff"/><path d="M4 3.5l2 1-1 1.5c.6 1.2 1.3 1.9 2.5 2.5L9 7.5l1 2-1.5 1C6 10 4 8 3.5 5.5z" fill="#fff"/></svg>555-214-3380</li>
      <li><svg class="icon" viewBox="0 0 14 14"><rect x=".5" y=".5" width="13" height="13" rx="2" fill="none" stroke="#fff"/><rect x="4.5" y="3" width="5" height="8" rx="1" fill="none" stroke="#fff"/></svg>555-762-1045(office)</li>
      <li><svg class="icon" viewBox="0 0 14 14"><rect x=".5" y=".5" width="13" height="13" rx="2" fill="none" stroke="#fff"/><rect x="3" y="4.5" width="8" height="5.5" fill="none" stroke="#fff"/><path d="M3 4.5l4 3 4-3" fill="none" stroke="#fff"/></svg>hello@verdantsolutionsco.com</li>
      <li><svg class="icon" viewBox="0 0 14 14"><rect x=".5" y=".5" width="13" height="13" rx="2" fill="none" stroke="#fff"/><circle cx="7" cy="7" r="3.5" fill="none" stroke="#fff"/><path d="M3.5 7h7M7 3.5v7" stroke="#fff"/></svg>www.verdantsolutionsco.com</li>
    </ul>
  </div>
</section>

<section class="set">
  <div class="card card-back"><div class="brand"><span class="brand-mark"></span>Verdant Solutions</div></div>
  <div class="card card-front">
    <svg class="shape" viewBox="0 0 530 300" aria-hidden="true">
      <polygon points="185,0 530,0 530,300 459,300" fill="#ffffff"/>
      <polygon points="178,0 185,0 459,300 450,300" fill="#8c8f94"/>
      <polygon points="0,58 230,58 283,117 0,117" fill="#8c8f94"/>
    </svg>
    <div class="person"><p class="person-name">Wade Dunmor</p><p class="person-title">Chief Technology Officer</p></div>
    <div class="brand"><span class="brand-mark"></span>Verdant Solutions</div>
    <ul class="contact">
      <li class="address">Harlow Crossing<br>Fenmore Park, 2240</li>
      <li><svg class="icon" viewBox="0 0 14 14"><rect x=".5" y=".5" width="13" height="13" rx="2" fill="none" stroke="#fff"/><path d="M4 3.5l2 1-1 1.5c.6 1.2 1.3 1.9 2.5 2.5L9 7.5l1 2-1.5 1C6 10 4 8 3.5 5.5z" fill="#fff"/></svg>555-214-3380</li>
      <li><svg class="icon" viewBox="0 0 14 14"><rect x=".5" y=".5" width="13" height="13" rx="2" fill="none" stroke="#fff"/><rect x="4.5" y="3" width="5" height="8" rx="1" fill="none" stroke="#fff"/></svg>555-762-1045(office)</li>
      <li><svg class="icon" viewBox="0 0 14 14"><rect x=".5" y=".5" width="13" height="13" rx="2" fill="none" stroke="#fff"/><rect x="3" y="4.5" width="8" height="5.5" fill="none" stroke="#fff"/><path d="M3 4.5l4 3 4-3" fill="none" stroke="#fff"/></svg>hello@verdantsolutionsco.com</li>
      <li><svg class="icon" viewBox="0 0 14 14"><rect x=".5" y=".5" width="13" height="13" rx="2" fill="none" stroke="#fff"/><circle cx="7" cy="7" r="3.5" fill="none" stroke="#fff"/><path d="M3.5 7h7M7 3.5v7" stroke="#fff"/></svg>www.verdantsolutionsco.com</li>
    </ul>
  </div>
</section>

</body>
</html>
```